Property Developer - Simple yet Sophisticated and Sharp Business Card

We are a medium sized property developer involved mainly in townhouse developments and land subdivisions.

The company is looking for a simple, sharp and sophisticated business card that will be given to contractors, land owners, financiers etc and thus will need to look professional.

Property development related graphics and art can be used, however the card is not to be too "busy" or crowded. Our company name is KL Estates which could possibly be incorporated into the graphics or artwork.

Single sided and/or double sided designs will be acceptable.

A Simple, Sophisticated, Sharp design please!

Good Luck !

```html
<!DOCTYPE html>
<html lang="en">
<head>
<meta charset="utf-8">
<title>KL Estates – Business Card Proposal</title>
<link rel="stylesheet" href="https://fonts.googleapis.com/css2?family=Arimo:wght@400;700&family=PT+Sans+Narrow:wght@700&family=PT+Sans:wght@400&display=swap">
<style>
  :root {
    --page: #ffffff;
    --ink: #111111;
    --card-dark: #222222;
    --card-light: #ffffff;
    --on-dark: #f2f2f2;
    --accent-grey: #c4c4c4;
    --frame: #1a1a1a;
  }
  * { margin: 0; padding: 0; box-sizing: border-box; }
  html, body { width: 1200px; height: 849px; overflow: hidden; background: var(--page); }
  .sheet { position: relative; width: 1200px; height: 849px; font-family: "Arimo", Arial, sans-serif; color: var(--ink); }

  .crop-marks { position: absolute; inset: 0; width: 1200px; height: 849px; }

  .card { position: absolute; overflow: hidden; }
  .card--dark { background: var(--card-dark); color: var(--on-dark); }
  .card--light { background: var(--card-light); border: 1.5px solid var(--frame); color: var(--ink); }
  .card--portrait { width: 262px; height: 380px; }
  .card--landscape { width: 381px; height: 262px; }

  .brand { position: absolute; display: flex; align-items: center; gap: 10px; }
  .brand__dot { width: 28px; height: 28px; border-radius: 50%; background: var(--accent-grey); flex: none; }
  .brand__name { font-family: "Arimo", Arial, sans-serif; font-weight: 700; font-size: 30px; letter-spacing: -0.5px; white-space: nowrap; }
  .card--dark .brand__name { color: var(--on-dark); }
  .card--light .brand__name { color: var(--ink); }

  .card--portrait .brand { left: 30px; top: 78px; }
  .card--landscape .brand { left: 26px; top: 70px; }

  .contact { position: absolute; font-size: 10px; line-height: 14.3px; list-style: none; }
  .card--portrait .contact { left: 0; right: 0; top: 306px; text-align: center; }
  .card--landscape .contact { right: 26px; top: 178px; text-align: right; }

  .proposal-label { position: absolute; left: 42px; top: 686px; }
  .proposal-label__intro { font-family: "PT Sans", Arial, sans-serif; font-size: 15px; color: var(--ink); }
  .proposal-label__client { font-family: "PT Sans Narrow", "Arial Narrow", sans-serif; font-weight: 700; font-size: 23px; margin-top: 5px; color: var(--ink); }
</style>
</head>
<body>
<main class="sheet">
  <svg class="crop-marks" viewBox="0 0 1200 849" aria-hidden="true">
    <line x1="0" y1="1" x2="50" y2="1" stroke="#111" stroke-width="1.5"/>
    <line x1="1" y1="799" x2="1" y2="849" stroke="#111" stroke-width="1.5"/>
    <line x1="1148" y1="848" x2="1200" y2="848" stroke="#111" stroke-width="1.5"/>
  </svg>

  <section class="card card--dark card--portrait" style="left:266px; top:67px;">
    <div class="brand"><span class="brand__dot"></span><span class="brand__name">KL Estates</span></div>
    <ul class="contact">
      <li>Phone: (07) 3000 4812</li>
      <li>Fax: (07) 3000 4813</li>
      <li>Email: projects.klestates@mailbox.com</li>
      <li>Postal: PO Box 2475 Marlow Heights QLD 4120</li>
    </ul>
  </section>

  <section class="card card--light card--portrait" style="left:745px; top:67px;">
    <div class="brand"><span class="brand__dot"></span><span class="brand__name">KL Estates</span></div>
    <ul class="contact">
      <li>Phone: (07) 3000 4812</li>
      <li>Fax: (07) 3000 4813</li>
      <li>Email: projects.klestates@mailbox.com</li>
      <li>Postal: PO Box 2475 Marlow Heights QLD 4120</li>
    </ul>
  </section>

  <section class="card card--dark card--landscape" style="left:266px; top:536px;">
    <div class="brand"><span class="brand__dot"></span><span class="brand__name">KL Estates</span></div>
    <ul class="contact">
      <li>Phone: (07) 3000 4812</li>
      <li>Fax: (07) 3000 4813</li>
      <li>Email: projects.klestates@mailbox.com</li>
      <li>Postal: PO Box 2475 Marlow Heights QLD 4120</li>
    </ul>
  </section>

  <section class="card card--light card--landscape" style="left:745px; top:536px;">
    <div class="brand"><span class="brand__dot"></span><span class="brand__name">KL Estates</span></div>
    <ul class="contact">
      <li>Phone: (07) 3000 4812</li>
      <li>Fax: (07) 3000 4813</li>
      <li>Email: projects.klestates@mailbox.com</li>
      <li>Postal: PO Box 2475 Marlow Heights QLD 4120</li>
    </ul>
  </section>

  <div class="proposal-label">
    <p class="proposal-label__intro">Business Cards Proposal for:</p>
    <p class="proposal-label__client">KL Estates</p>
  </div>
</main>
</body>
</html>
```